Business card design needed for a security services business.

We provide a wide range of security services from guard personnel to electronic systems.

Industry/Entity Type

Security Industry

Contact Information for Business Card

Brent Holloway, Owner Office: 780.555.0148; Cell: 780.555.0193 Email: brent@korvanshieldgroup.example; Address 20417 163 St Edmonton, AB T5X 2K8

Colors
0054AA
0677BA
7BADD7
CADEEF
E8F1F8

Requirements
Nice to have
• On the back of the card I would like to possible list the services I provide: Guards Mobiles Live Video Surveillance Access Intrusion

```html
<!DOCTYPE html>
<html lang="en">
<head>
<meta charset="utf-8">
<title>Korvan Shield Group — Business Card</title>
<link href="https://fonts.googleapis.com/css2?family=Roboto+Condensed:wght@300;400;700&display=swap" rel="stylesheet">
<style>
  :root {
    --blue: #0677BA;
    --blue-deep: #0054AA;
    --grey: #5f6062;
    --grey-light: #8a8b8d;
    --rule: #6b6b6b;
    --paper: #ffffff;
    --backdrop: #d6d6d6;
  }
  * { margin: 0; padding: 0; box-sizing: border-box; }
  html, body {
    width: 1200px; height: 846px; overflow: hidden;
    background: var(--backdrop);
    font-family: "Roboto Condensed", "Arial Narrow", sans-serif;
  }
  .stage {
    width: 1200px; height: 846px;
    display: flex; align-items: center; justify-content: center; gap: 40px;
  }
  .card {
    width: 540px; height: 309px; position: relative; overflow: hidden;
    box-shadow: 0 6px 18px rgba(0,0,0,.18);
  }
  .brand {
    display: flex; align-items: center; gap: 8px; white-space: nowrap;
  }
  .brand__mark { width: 14px; height: 14px; flex: none; }
  .brand__name {
    font-weight: 700; text-transform: uppercase; line-height: 1; letter-spacing: .3px;
  }
  .brand-rule { height: 2px; }

  /* Front */
  .card--front { background: var(--paper); }
  .front-brand {
    position: absolute; left: 30px; top: 168px; width: 256px;
  }
  .card--front .brand__mark { background: var(--blue); }
  .card--front .brand__name { color: var(--blue); font-size: 22px; }
  .card--front .brand-rule { background: var(--rule); margin: 10px 0 0 22px; width: 214px; }
  .divider {
    position: absolute; left: 300px; top: 70px;
    width: 1px; height: 140px; background: #9a9a9a;
  }
  .contact {
    position: absolute; left: 314px; top: 72px; width: 214px;
    font-size: 13.5px; line-height: 1.5; color: var(--grey);
    font-weight: 300; white-space: nowrap;
  }
  .contact__name { color: var(--blue); font-weight: 700; font-size: 15px; margin-bottom: 6px; }
  .contact__role { color: var(--grey-light); font-weight: 300; }
  .contact__label { color: var(--blue); font-weight: 700; }

  /* Back */
  .card--back { background: var(--blue); color: #fff; }
  .back-brand {
    position: absolute; left: 0; right: 0; top: 52px;
    display: flex; flex-direction: column; align-items: center;
  }
  .card--back .brand__mark { background: #fff; }
  .card--back .brand__name { color: #fff; font-size: 30px; }
  .card--back .brand-rule { background: #fff; margin-top: 10px; width: 300px; }
  .services {
    position: absolute; left: 18px; right: 18px; bottom: 40px;
    display: flex; justify-content: space-between; list-style: none;
  }
  .service { width: 78px; text-align: center; }
  .service svg { width: 40px; height: 40px; display: block; margin: 0 auto 10px; fill: #fff; }
  .service__label {
    font-size: 11px; line-height: 1.2; text-transform: uppercase; font-weight: 400;
  }
</style>
</head>
<body>
<main class="stage">
  <section class="card card--front" aria-label="Card front">
    <div class="front-brand">
      <div class="brand">
        <span class="brand__mark"></span>
        <span class="brand__name">Korvan Shield Group</span>
      </div>
      <div class="brand-rule"></div>
    </div>
    <div class="divider"></div>
    <div class="contact">
      <p class="contact__name">Brent Holloway <span class="contact__role">Owner</span></p>
      <p><span class="contact__label">Office:</span> 780.555.0148</p>
      <p><span class="contact__label">Cell:</span> 780.555.0193</p>
      <p>brent@korvanshieldgroup.example</p>
      <p>20417 163 St Edmonton, AB T5X 2K8</p>
    </div>
  </section>

  <section class="card card--back" aria-label="Card back">
    <div class="back-brand">
      <div class="brand">
        <span class="brand__mark"></span>
        <span class="brand__name">Korvan Shield Group</span>
      </div>
      <div class="brand-rule"></div>
    </div>
    <ul class="services">
      <li class="service">
        <svg viewBox="0 0 40 40" aria-hidden="true"><path d="M8 4h24v34H8z M12 9v4h4V9z M18 9v4h4V9z M24 9v4h4V9z M12 16v4h4v-4z M18 16v4h4v-4z M24 16v4h4v-4z M12 23v4h4v-4z M18 23v4h4v-4z M24 23v4h4v-4z" fill-rule="evenodd"/></svg>
        <p class="service__label">Exterior &amp;<br>Interior Patrols</p>
      </li>
      <li class="service">
        <svg viewBox="0 0 40 40" aria-hidden="true"><path d="M10 8h20l5 12v12h-5v4h-5v-4H15v4h-5v-4H5V20z M12 12l-3 8h22l-3-8z M9 23v4h5v-4z M26 23v4h5v-4z" fill-rule="evenodd"/></svg>
        <p class="service__label">Incident<br>Response</p>
      </li>
      <li class="service">
        <svg viewBox="0 0 40 40" aria-hidden="true"><circle cx="13" cy="12" r="6"/><circle cx="28" cy="12" r="6"/><path d="M2 34v-6a8 8 0 0 1 8-8h6a8 8 0 0 1 8 8v6z"/><path d="M26 20h5a8 8 0 0 1 8 8v6H27v-6a10 10 0 0 0-3-7z"/></svg>
        <p class="service__label">Safety<br>Escorts</p>
      </li>
      <li class="service">
        <svg viewBox="0 0 40 40" aria-hidden="true"><circle cx="13" cy="11" r="6"/><path d="M2 34v-6a8 8 0 0 1 8-8h8v14z"/><path d="M28 14l10 3v7c0 6-4 10-10 12-6-2-10-6-10-12v-7z"/></svg>
        <p class="service__label">Alarm<br>Response</p>
      </li>
      <li class="service">
        <svg viewBox="0 0 40 40" aria-hidden="true"><circle cx="12" cy="12" r="6"/><path d="M2 34v-6a8 8 0 0 1 8-8h8v14z"/><path d="M24 20v-4a6 6 0 0 1 12 0v4h2v14H22V20z M27 20h6v-4a3 3 0 0 0-6 0z" fill-rule="evenodd"/></svg>
        <p class="service__label">Lock &amp;<br>Unlock</p>
      </li>
      <li class="service">
        <svg viewBox="0 0 40 40" aria-hidden="true"><path d="M10 4l10 9v6h-3v15H3V19H0v-6z"/><path d="M20 14h18v16H20z M23 17v10h12V17z" fill-rule="evenodd"/><path d="M18 31h22v3H18z"/></svg>
        <p class="service__label">Online<br>Reporting</p>
      </li>
    </ul>
  </section>
</main>
</body>
</html>
```